post card 4x6

this is a post card that will be sent to plumbing companies and foundation repair companies for whole sale work. if you can add ( work done in unmarked truck -will ware your shirt)

```html
<!DOCTYPE html>
<html lang="en">
<head>
<meta charset="utf-8">
<title>DrainView Wholesale Postcard</title>
<link href="https://fonts.googleapis.com/css2?family=Poppins:wght@500;600;700;800&display=swap" rel="stylesheet">
<style>
:root{
  --page:#e9e9e9;
  --navy:#232a37;
  --navy-deep:#1b2029;
  --red:#e84c3d;
  --white:#ffffff;
  --ink:#232a37;
  --stamp:#e6e6e6;
  --rule:#c9c9c9;
}
*{margin:0;padding:0;box-sizing:border-box}
html,body{width:1200px;height:2548px;overflow:hidden;background:var(--page);font-family:'Poppins',sans-serif}
.card{position:absolute;left:96px;width:1008px;height:673px;overflow:hidden;box-shadow:0 6px 14px rgba(0,0,0,.18)}
.abs{position:absolute}
.front{top:997px;background:var(--white)}
.back{top:1746px;background:var(--white)}
.shapes{position:absolute;left:0;top:0}
.brand{font-weight:800;color:var(--red);letter-spacing:1px;white-space:nowrap}
.front .brand{left:62px;top:38px;font-size:58px}
.hero-photo{left:560px;top:26px;width:448px;height:399px;background:linear-gradient(135deg,#5a5f68 0%,#8a8f96 35%,#2c4fb0 60%,#3a3f48 100%)}
.kicker{left:43px;top:150px;font-size:27px;font-weight:600;color:var(--white)}
.headline{left:43px;top:188px;font-size:69px;font-weight:800;line-height:71px;color:var(--white)}
.headline .accent{color:var(--red)}
.service-band{left:0;top:425px;width:1008px;height:90px;background:var(--red)}
.service-col{position:absolute;top:16px;color:var(--white);font-size:18.5px;font-weight:600;line-height:29px}
.service-col li{list-style:none;display:flex;align-items:center;gap:8px}
.service-col svg{flex:none}
.col-divider{position:absolute;top:18px;width:2px;height:58px;background:rgba(255,255,255,.45)}
.call-pill{left:48px;top:535px;width:224px;height:38px;background:var(--red);border-radius:10px;color:var(--white);font-size:27px;font-weight:700;line-height:38px;text-align:center;letter-spacing:.5px}
.front-phone{left:48px;top:578px;font-size:41px;font-weight:700;color:var(--white);display:flex;align-items:center;gap:8px}
.truck-pill{left:452px;top:550px;width:512px;height:36px;border:2px solid var(--navy);border-radius:12px;background:var(--navy);display:flex;overflow:hidden;font-size:18.5px;font-weight:600}
.truck-pill .lead{background:var(--white);color:var(--ink);padding:0 8px;border-radius:10px;line-height:32px}
.truck-pill .tail{color:var(--white);padding:0 12px;line-height:32px}
.front-web{left:490px;top:607px;width:518px;text-align:center;color:var(--white);font-size:19px;font-weight:600;letter-spacing:6.5px}
/* back */
.back-panel{left:0;top:0;width:590px;height:673px;background:var(--navy)}
.tagline{left:50px;top:38px;font-size:45px;font-weight:800;line-height:44px;color:var(--white)}
.tagline .accent{color:var(--red)}
.services-band{left:0;top:143px;width:605px;height:190px;background:var(--red)}
.services-title{left:48px;top:145px;font-size:29px;font-weight:800;color:var(--ink);letter-spacing:.3px}
.svc{position:absolute;display:flex;align-items:center;gap:10px;color:var(--white);font-size:19px;font-weight:600;line-height:22px}
.svc-icon{width:36px;height:36px;border-radius:50%;background:var(--navy);border:2px solid var(--white);flex:none}
.svc-divider{left:320px;top:198px;width:2px;height:128px;background:rgba(255,255,255,.45)}
.inspection-photo{top:345px;width:258px;height:154px;border:3px solid var(--white)}
.photo-root{left:48px;background:radial-gradient(circle at 45% 45%,#2a1a12 0%,#6b4526 30%,#c8925c 70%,#8a5a34 100%)}
.photo-lined{left:316px;background:radial-gradient(circle at 30% 40%,#1e3a2e 0%,#3f8a68 35%,#6bb08e 70%,#2f6b52 100%)}
.wholesale-box{left:48px;top:517px;width:462px;height:36px;border:2px solid var(--white);color:var(--white);font-size:27px;font-weight:700;line-height:32px;padding-left:9px;white-space:nowrap}
.wholesale-box .accent{color:var(--red)}
.contact-line{left:48px;display:flex;align-items:center;gap:8px;color:var(--white);font-size:21px;font-weight:600}
.rmp{background:var(--red);border-radius:10px;padding:0 8px;font-size:18px;line-height:24px;margin-left:6px}
.back .brand{left:620px;top:46px;font-size:42px}
.stamp-box{left:882px;top:46px;width:78px;height:84px;background:var(--stamp)}
.address-rule{left:620px;width:342px;height:1px;background:var(--rule)}
</style>
</head>
<body>

<!-- FRONT -->
<section class="card front">
  <svg class="shapes" width="1008" height="673" viewBox="0 0 1008 673">
    <rect x="0" y="26" width="1008" height="399" fill="#232a37"/>
    <polygon points="0,0 448,0 368,124 0,124" fill="#ffffff"/>
    <polygon points="452,0 1008,0 1008,26 436,26" fill="#e84c3d"/>
    <polygon points="0,556 400,556 483,673 0,673" fill="#232a37"/>
    <polygon points="440,596 1008,596 1008,673 494,673" fill="#e84c3d"/>
  </svg>
  <div class="abs hero-photo" role="img" aria-label="Plumber in blue overalls fixing pipes under a kitchen sink"></div>
  <svg class="shapes" width="1008" height="130" viewBox="0 0 1008 130">
    <polygon points="0,0 448,0 368,124 0,124" fill="#ffffff"/>
  </svg>
  <div class="abs brand">DrainView</div>
  <div class="abs kicker">YOUR ONE-STOP SOLUTION FOR</div>
  <h1 class="abs headline">PLUMBING &amp;<br><span class="accent">IRRIGATION</span><br>INSTALLATION</h1>

  <div class="abs service-band">
    <ul class="service-col" style="left:48px">
      <li><svg width="20" height="20" viewBox="0 0 20 20"><circle cx="10" cy="10" r="6" fill="none" stroke="#fff" stroke-width="3" stroke-dasharray="3 2"/><circle cx="10" cy="10" r="2.5" fill="#fff"/></svg>CIPP (CURED IN PLACE PIPE)</li>
      <li><svg width="20" height="20" viewBox="0 0 20 20"><circle cx="10" cy="10" r="6" fill="none" stroke="#fff" stroke-width="3" stroke-dasharray="3 2"/><circle cx="10" cy="10" r="2.5" fill="#fff"/></svg>HYDRO JETTING</li>
    </ul>
    <div class="col-divider" style="left:362px"></div>
    <ul class="service-col" style="left:392px">
      <li><svg width="20" height="20" viewBox="0 0 20 20"><circle cx="10" cy="10" r="6" fill="none" stroke="#fff" stroke-width="3" stroke-dasharray="3 2"/><circle cx="10" cy="10" r="2.5" fill="#fff"/></svg>SIPP (SPRAY IN PLACE PIPE)</li>
      <li><svg width="20" height="20" viewBox="0 0 20 20"><circle cx="10" cy="10" r="6" fill="none" stroke="#fff" stroke-width="3" stroke-dasharray="3 2"/><circle cx="10" cy="10" r="2.5" fill="#fff"/></svg>SEWER CAMERA AND LOCATE</li>
    </ul>
    <div class="col-divider" style="left:737px"></div>
    <ul class="service-col" style="left:766px">
      <li><svg width="20" height="20" viewBox="0 0 20 20"><circle cx="10" cy="10" r="6" fill="none" stroke="#fff" stroke-width="3" stroke-dasharray="3 2"/><circle cx="10" cy="10" r="2.5" fill="#fff"/></svg>PIPE BURSTING</li>
      <li><svg width="20" height="20" viewBox="0 0 20 20"><circle cx="10" cy="10" r="6" fill="none" stroke="#fff" stroke-width="3" stroke-dasharray="3 2"/><circle cx="10" cy="10" r="2.5" fill="#fff"/></svg>RESIZE CAST IRON</li>
    </ul>
  </div>

  <div class="abs call-pill">CALL US NOW</div>
  <div class="abs front-phone">
    <svg width="34" height="34" viewBox="0 0 34 34"><circle cx="17" cy="17" r="16" fill="#e84c3d"/><path d="M11 9c1-1 3-1 4 1l1 3c0 1-1 2-2 2 1 2 3 4 5 5 0-1 1-2 2-2l3 1c2 1 2 3 1 4-2 2-5 2-9-1s-6-7-6-9c0-2 0-3 1-4z" fill="#fff"/></svg>
    555-014-2277
  </div>
  <div class="abs truck-pill"><span class="lead">Work done in unmarked truck</span><span class="tail">will ware your shirt</span></div>
  <div class="abs front-web">www.drainviewplumbing.com</div>
</section>

<!-- BACK -->
<section class="card back">
  <div class="abs back-panel"></div>
  <h2 class="abs tagline"><span class="accent">YOU MAKE THE $</span><br>WE DO THE WORK</h2>
  <div class="abs services-band"></div>
  <svg class="shapes" width="300" height="190" viewBox="0 0 300 190">
    <polygon points="0,143 272,143 286,182 0,182" fill="#ffffff"/>
    <line x1="277" y1="143" x2="292" y2="182" stroke="#ffffff" stroke-width="3"/>
  </svg>
  <div class="abs services-title">OUR SERVICES</div>

  <div class="svc" style="left:52px;top:200px"><span class="svc-icon"></span><span>Drain and Pipe<br>Repair and Cleaning</span></div>
  <div class="svc" style="left:52px;top:256px"><span class="svc-icon"></span><span>Hydro Jetting</span></div>
  <div class="svc" style="left:52px;top:299px"><span class="svc-icon"></span><span>Pipe Bursting</span></div>
  <div class="abs svc-divider"></div>
  <div class="svc" style="left:347px;top:200px"><span class="svc-icon"></span><span>Sewer Video<br>Inspection</span></div>
  <div class="svc" style="left:347px;top:256px"><span class="svc-icon"></span><span>Pipe Lining</span></div>

  <div class="abs inspection-photo photo-root" role="img" aria-label="Camera view inside a sewer pipe with root intrusion"></div>
  <div class="abs inspection-photo photo-lined" role="img" aria-label="Camera view inside a newly lined green pipe"></div>

  <div class="abs wholesale-box">CALL FOR <span class="accent">WHOLE SALE PRICING</span></div>
  <div class="abs contact-line" style="top:565px">
    <svg width="20" height="20" viewBox="0 0 34 34"><circle cx="17" cy="17" r="16" fill="#e84c3d"/><path d="M11 9c1-1 3-1 4 1l1 3c0 1-1 2-2 2 1 2 3 4 5 5 0-1 1-2 2-2l3 1c2 1 2 3 1 4-2 2-5 2-9-1s-6-7-6-9c0-2 0-3 1-4z" fill="#fff"/></svg>
    555-014-2277
  </div>
  <div class="abs contact-line" style="top:592px">
    <svg width="20" height="20" viewBox="0 0 20 20"><circle cx="10" cy="10" r="8" fill="none" stroke="#e84c3d" stroke-width="2"/><path d="M2 10h16M10 2c-4 4-4 12 0 16M10 2c4 4 4 12 0 16" fill="none" stroke="#e84c3d" stroke-width="1.5"/></svg>
    www.drainviewplumbing.com <span class="rmp">RMP#10293</span>
  </div>

  <div class="abs brand">DrainView</div>
  <div class="abs stamp-box"></div>
  <div class="abs address-rule" style="top:308px"></div>
  <div class="abs address-rule" style="top:362px"></div>
  <div class="abs address-rule" style="top:415px"></div>
</section>

</body>
</html>
```